Letterhead and compliment slip

We are a UK-based market research agency. We are looking for a new letterhead design to incorporate our logo, address details and company information. We are looking for a simple design. It should be modern. It needs to have a qualify feel. As we are UK based it needs to be designed for A4 paper size (letterhead).
I'm really looking for something simple in design terms!
Both letterhead and compliment slip need to include:
Our logo
Company address
Telephone number
Email address
Website address
Company registration number
VAT registration number
Grey and green would be a good colour scheme to fit with our logo

```html
<!DOCTYPE html>
<html lang="en">
<head>
<meta charset="utf-8">
<title>Quillmere Consumer Research – Letterhead</title>
<link href="https://fonts.googleapis.com/css2?family=Arimo:ital,wght@0,400;0,700;1,700&family=Roboto:wght@700&family=Roboto+Condensed:wght@400;500&family=Yellowtail&family=Dancing+Script:wght@500&display=swap" rel="stylesheet">
<style>
  :root {
    --green: #9bc23c;
    --grey: #9a9a9a;
    --ink: #1e1e1e;
    --paper: #ffffff;
    --backdrop: #e9e9e6;
  }
  * { box-sizing: border-box; margin: 0; padding: 0; }
  html, body { width: 1189px; height: 1200px; overflow: hidden; }
  body { background: var(--backdrop); position: relative; }

  .letterhead {
    position: absolute; left: 138px; top: 9px;
    width: 912px; height: 1182px;
    background: var(--paper);
    box-shadow: 0 2px 10px rgba(0,0,0,.15);
    font-family: "Roboto Condensed", "Arial Narrow", sans-serif;
    color: var(--ink);
  }

  .brand {
    position: absolute; top: 80px; left: 0; width: 100%;
    display: flex; justify-content: center; align-items: center; gap: 14px;
  }
  .brand-dot { width: 44px; height: 44px; border-radius: 50%; background: var(--green); }
  .brand-name {
    font-family: "Roboto", sans-serif; font-weight: 700;
    font-size: 54px; color: var(--green); letter-spacing: -0.5px; line-height: 1;
  }

  .recipient { position: absolute; left: 76px; top: 306px; }
  .recipient-name { font-size: 20px; font-weight: 500; text-transform: uppercase; margin-bottom: 8px; }
  .recipient-address { font-size: 16px; line-height: 21px; }

  .letter-body {
    position: absolute; left: 77px; top: 437px; width: 760px;
    font-size: 17.5px; line-height: 29px; text-align: justify;
  }
  .letter-body p + p { margin-top: 29px; }
  .closing { position: absolute; left: 76px; top: 812px; font-size: 17.5px; }

  .signature {
    position: absolute; left: 76px; top: 888px;
    font-family: "Yellowtail", "Dancing Script", cursive; font-size: 60px; line-height: 1; color: var(--ink);
  }
  .signatory { position: absolute; left: 76px; top: 978px; font-size: 19px; font-weight: 500; line-height: 22px; }

  .company-details {
    position: absolute; left: 0; top: 1084px; width: 100%;
    text-align: center; font-family: "Arimo", Arial, sans-serif;
    font-size: 12.5px; line-height: 17px; color: var(--grey);
  }
  .company-name { color: var(--green); font-weight: 700; font-size: 13px; }
  .label { color: var(--green); font-weight: 700; font-style: italic; }
  .accent { color: var(--green); }

  .registration-tab {
    position: absolute; left: 175px; top: 1157px; width: 560px; height: 25px;
    background: var(--green); border-radius: 14px 14px 0 0;
    font-family: "Arimo", Arial, sans-serif; font-style: italic; font-weight: 700;
    font-size: 12.5px; color: #fff; text-align: center; line-height: 24px; word-spacing: 2px;
  }
  .base-rule { position: absolute; left: 0; bottom: 0; width: 100%; height: 3px; background: var(--green); }
</style>
</head>
<body>
  <main class="letterhead">
    <header class="brand">
      <span class="brand-dot"></span>
      <span class="brand-name">Quillmere</span>
    </header>

    <section class="recipient">
      <div class="recipient-name">John Smith</div>
      <div class="recipient-address">Street Name,City Name.<br>Zip Coad 0000</div>
    </section>

    <section class="letter-body">
      <p>Lorem Ipsum is simply dummy text of the printing and typesetting industry. Lorem Ipsum has been the industry’s standard dummy text ever since the 1500s, when an unknown printer took a galley of type and scrambled it to make a type specimen book. It has survived not only five centuries,but also the leap into electronic typesetting, remaining essentially unchanged. It was popularised in the 1960s with the release of Letraset sheets containing Lorem Ipsum passages, and more recently with desktop publishing software like Aldus PageMaker including versions of Lorem Ipsum.</p>
      <p>It is a long established fact that a reader will be distracted by the readable content of a page when looking at its layout. The point of using Lorem Ipsum is that it has a more-or-less normal distribution of letters, as opposed to using ’Content here, content here’, making it look like readable English. Many desktop publishing packages and web page editors now use Lorem Ipsum as their default model text, and a search for ’lorem ipsum’ will uncover many web sites still in their infancy. Various versions have evolved over the years, sometimes by accident, sometimes on purpose (injected humour and the like).</p>
    </section>
    <div class="closing">Regards,</div>

    <div class="signature">John Doe</div>
    <div class="signatory">John Doe<br>General Maneger</div>

    <footer class="company-details">
      <div class="company-name">Quillmere Consumer Research Ltd.</div>
      <div>4 Larkspur Yard, Fenwick Row, Little Amberford, Hertfordshire, ZZ9 9ZZ</div>
      <div><span class="label">P:</span> +44 (0)1632 960 418 | <span class="label">E:</span> hello@quillmereresearch.example</div>
      <div>www.<span class="accent">quillmereresearch</span>.example</div>
    </footer>
    <div class="registration-tab">Company registration number: &nbsp;0000000 &nbsp;| &nbsp;VAT registration number: &nbsp;000000000</div>
    <div class="base-rule"></div>
  </main>
</body>
</html>
```